HTML Digital Sign layout and code (one page)...save us from the 60's!

Digital Sign for Headquarters Entrance

HTML Digital Sign layout (one page)...save us from the 60's!

Good Day Designers!

We have decided to install Digital Signage in our headquarters building that will replace the “felt boards” that the administrative staff use at our building entrances.

Instead of the information being displayed on the archaic sign boards, it will be presented on a landscaped 50inch LCD screen running at 1920x1080

We are looking for a one page HTML design that encompass the following elements:

+ Our Logo
+ Our Company Name (Vorlan Aerotek)
+ Our "Tag Line" - "Progress Shaped By Practice, Quality Shaped By Dedication"
+ Date and Time
+ A space for Today’s Birthdays (which could be up to 4 people)
+ A space for Today’s Anniversaries (which could be up to 4 people)
+ A space for Today’s Visitor (which could be up to 2 people)
+ A space for a Picture of the Day
+ A space for Weather Forecast (perhaps a graphic)
+ A small "banner" section or strip for scrolling Notices / Alerts (perhaps at the bottom of the page?)

The deliverables for the layout need to include the HTML, applicable CSS, HTML code, etc. We need this to be relatively turnkey.

I have included in the contest package a hi-res JPG and AI for our Company Logo.

From a color pallet perspective:

Light Blue:
RGB - 21, 191,242
HEX - #15BFF2

Dark Blue:
RGB - 0, 70, 154
HEX - #00469A

Additionally, I have done a contest like this before (for another company I was at) and have included a screen shot of that final display.

PLEASE NOTE: IT DOES NOT HAVE TO LOOK EXACTLY LIKE THE ATTACHED SCREEN SHOT FROM THE PREVIOUS CONTEST. Including the screenshot was just to give you a general idea of some inspiration and objectives.

Feedback and questions are encouraged.

Target Market(s)

Our Employees

Industry/Entity Type

Digital

Number of Pages Required

1 page

Requirements
Must have
• + Our Logo
• + Our Company Name (Vorlan Aerotek)
• + Our "Tag Line" - "Progress Shaped By Practice, Quality Shaped By Dedication"
• + Date and Time
• + A space for Today’s Birthdays (which could be up to 4 people)
• + A space for Today’s Anniversaries (which could be up to 4 people)
• + A space for Today’s Visitor (which could be up to 2 people)
• + A space for a Picture of the Day
• + A space for Weather Forecast (perhaps a graphic)
• + A small "banner" section or strip for scrolling Notices / Alerts (perhaps at the bottom of the page?)

```html
<!DOCTYPE html>
<html lang="en">
<head>
<meta charset="utf-8">
<title>Vorlan Aerotek – Entrance Sign</title>
<link rel="stylesheet" href="https://fonts.googleapis.com/css2?family=Arimo:wght@400;700&display=swap">
<style>
  :root {
    --dark-blue: #00469A;
    --light-blue: #15BFF2;
    --sky-top: #1bb6ee;
    --sky-low: #d8f1fc;
    --panel-border: #2d6fd0;
    --text-grey: #555a60;
    --muted: #c4c7cb;
    --white: #ffffff;
  }
  * { box-sizing: border-box; margin: 0; padding: 0; }
  html, body { width: 1200px; height: 675px; overflow: hidden; }
  body {
    font-family: "Arimo", Arial, sans-serif;
    background: linear-gradient(180deg, var(--sky-top) 0%, #6fd2f5 22%, var(--sky-low) 45%, #eaf7fd 100%);
    position: relative;
  }
  .brand {
    position: absolute; left: 40px; top: 30px; width: 270px;
    text-align: center; color: var(--dark-blue);
    font-weight: 700; font-size: 34px; letter-spacing: 0.5px;
    line-height: 58px;
  }
  .header-divider {
    position: absolute; left: 375px; top: 16px; width: 1px; height: 86px;
    background: rgba(255,255,255,0.55);
  }
  .tagline {
    position: absolute; left: 390px; top: 22px; width: 760px;
    text-align: center; color: var(--white);
    font-weight: 700; font-size: 31px; line-height: 40px;
  }
  .panel {
    position: absolute; background: var(--white);
    border: 1px solid var(--panel-border); border-radius: 8px; overflow: hidden;
  }
  .panel-title {
    height: 48px; background: var(--dark-blue); color: var(--white);
    font-weight: 700; font-size: 26px; line-height: 50px; padding-left: 20px;
  }
  .name-list { list-style: none; padding: 12px 0 0 25px; }
  .name-list li { font-size: 18px; color: var(--text-grey); line-height: 37.5px; }
  .picture-panel { left: 17px; top: 122px; width: 380px; height: 388px; }
  .birthdays-panel { left: 411px; top: 122px; width: 380px; height: 224px; }
  .anniversaries-panel { left: 805px; top: 122px; width: 379px; height: 224px; }
  .visitors-panel { left: 411px; top: 357px; width: 380px; height: 153px; }
  .visitors-panel .name-list { padding-left: 23px; padding-top: 12px; }
  .weather-panel { left: 805px; top: 357px; width: 379px; height: 153px; }
  .photo {
    position: absolute; left: 21px; top: 63px; width: 334px; height: 222px;
    background: linear-gradient(180deg, #4a3e55 0%, #7b5a52 22%, #3b3a3d 45%, #8f8a80 62%, #5a4f45 80%, #2c2a2c 100%);
  }
  .photo-label {
    position: absolute; left: 0; right: 0; bottom: 14px; text-align: center;
    color: rgba(255,255,255,0.45); font-size: 18px;
  }
  .caption-title {
    position: absolute; left: 21px; top: 299px;
    color: var(--dark-blue); font-size: 18px;
  }
  .caption-body {
    position: absolute; left: 21px; top: 320px; width: 334px;
    color: #222; font-size: 12.5px; line-height: 15.5px;
  }
  .weather-placeholder {
    text-align: center; color: var(--muted); font-size: 20px; padding-top: 38px;
  }
  .notice-strip { left: 17px; top: 520px; width: 1167px; height: 107px; }
  .footer {
    position: absolute; left: 0; top: 636px; width: 1200px; height: 39px;
    background: var(--dark-blue); color: var(--white);
    font-weight: 700; font-size: 20px; line-height: 40px;
    display: flex; justify-content: space-between; padding: 0 14px 0 8px;
  }
  .date-time { font-weight: 400; font-size: 18px; }
</style>
</head>
<body>
  <div class="brand">Vorlan Aerotek</div>
  <div class="header-divider"></div>
  <h1 class="tagline">Progress Shaped By Practice,<br>Quality Shaped By Dedication</h1>

  <section class="panel picture-panel">
    <h2 class="panel-title">Picture of the Day</h2>
    <div class="photo" role="img" aria-label="Picture of the day: aircraft parked in a lit hangar at dusk">
      <span class="photo-label">&lt; Sample Image &gt;</span>
    </div>
    <p class="caption-title">Image brief description</p>
    <p class="caption-body">Lorem ipsum dolor sit amet lorem ipsum dolor sit lor sit amet lorem ipsum dolor sit lorem ipsum lorem ips dolor sum dolor sit amet lorem ipsum.</p>
  </section>

  <section class="panel birthdays-panel">
    <h2 class="panel-title">Today’s Birthdays</h2>
    <ul class="name-list">
      <li>First Name, Last Name one</li>
      <li>First Name, Last Name two</li>
      <li>First Name, Last Name three</li>
      <li>First Name, Last Name four</li>
    </ul>
  </section>

  <section class="panel anniversaries-panel">
    <h2 class="panel-title">Today’s Anniversaries</h2>
    <ul class="name-list">
      <li>First Name, Last Name one</li>
      <li>First Name, Last Name two</li>
      <li>First Name, Last Name three</li>
      <li>First Name, Last Name four</li>
    </ul>
  </section>

  <section class="panel visitors-panel">
    <h2 class="panel-title">Today’s Visitors</h2>
    <ul class="name-list">
      <li>First Name, Last Name one</li>
      <li>First Name, Last Name two</li>
    </ul>
  </section>

  <section class="panel weather-panel">
    <h2 class="panel-title">Weather Forecast</h2>
    <p class="weather-placeholder">(Weather Forecast Graphic Here)</p>
  </section>

  <section class="panel notice-strip" aria-label="Notices and alerts"></section>

  <footer class="footer">
    <span>© Vorlan Aerotek LTD 2014</span>
    <time class="date-time" datetime="2014-06-02T09:30">Monday, June 2, 2014 · 9:30 AM</time>
    <span>www.vorlanaerotek.com</span>
  </footer>
</body>
</html>
```